brell carpentry & property maintenance

busines card for my carpentry business
easy to read
not to bogged out with to much info
I like the colour bule baby blue ish
repair it build it fix it
all aspects of carpentry and joinery
building work no job to small

Reason: I can not seem to get my logo to you guys could I have an email address please to send to thanks owen

Target Market(s)

home owners unit blocks people to busy to look after yard

Industry/Entity Type

Property Maintenance

Contact Information for Business Card

email: brellcarpentry@mailvane.com.au
phone 0427351846
Owen Brell qualified carpenter

Logo Text

brell carpentry $ property mainteaince

Logo styles of interest
Lettermark Logo
Requirements
Must have
• thinking logo front and back a blue print type sketch plans over card
would like logo to have B W like the one that I have on my file
I can not get the look n feel tool bare to work but it should be pointing more to the pro bold up market theme
my lic no 473152c
my name Owen Brell qualified carpenter
fully insured
Nice to have
• front int BW with Brell carpentry & property maintenance written through

```html
<!DOCTYPE html>
<html lang="en">
<head>
<meta charset="utf-8">
<title>Brell Carpentry – Business Card</title>
<link rel="stylesheet" href="https://fonts.googleapis.com/css2?family=EB+Garamond:wght@400;700&family=Open+Sans:wght@700;800&display=swap">
<style>
  :root {
    --sky-light: #d6f5fd;
    --sky-mid: #7fd8f6;
    --sky-edge: #1fb4ec;
    --ink: #231f20;
    --band-navy: #0b3b6b;
    --white: #ffffff;
  }
  html, body {
    margin: 0;
    padding: 0;
    overflow: hidden;
    background: #e9eef2;
  }
  .card {
    position: relative;
    width: 1200px;
    height: 734px;
    overflow: hidden;
    background: radial-gradient(ellipse 70% 75% at 52% 58%, var(--sky-light) 0%, var(--sky-mid) 55%, var(--sky-edge) 100%);
    color: var(--ink);
  }
  .brand {
    position: absolute;
    left: 268px;
    top: 70px;
    width: 662px;
    text-align: center;
    font-family: "Open Sans", Arial, sans-serif;
    font-weight: 800;
    font-size: 82px;
    line-height: 1;
    letter-spacing: 1px;
    text-transform: uppercase;
    color: var(--ink);
  }
  .brand-sub {
    display: block;
    margin-top: 14px;
    font-size: 44px;
    letter-spacing: 22px;
  }
  .person {
    position: absolute;
    left: 0;
    width: 1200px;
    top: 318px;
    text-align: center;
    font-family: "EB Garamond", Georgia, serif;
  }
  .person-name {
    margin: 0;
    font-weight: 700;
    font-size: 48px;
    line-height: 1.1;
  }
  .person-role {
    margin: 10px 0 0;
    font-weight: 400;
    font-size: 41px;
    letter-spacing: 1.5px;
    line-height: 1.1;
  }
  .person-licence {
    margin: 6px 0 0;
    font-size: 21px;
    letter-spacing: 0.5px;
  }
  .contact {
    position: absolute;
    right: 41px;
    top: 502px;
    text-align: right;
    font-family: "EB Garamond", Georgia, serif;
    font-size: 40px;
    line-height: 1.4;
  }
  .contact p { margin: 0; }
  .tagline-band {
    position: absolute;
    left: 0;
    bottom: 0;
    width: 1200px;
    height: 104px;
    background: var(--band-navy);
    color: var(--white);
    font-family: "Open Sans", Arial, sans-serif;
    font-weight: 700;
    font-size: 47px;
    line-height: 104px;
  }
  .tagline {
    position: absolute;
    top: 0;
    white-space: nowrap;
  }
  .tagline--repair { left: 41px; }
  .tagline--build { left: 638px; transform: translateX(-50%); }
  .tagline--fix { right: 43px; }
</style>
</head>
<body>
  <main class="card">
    <div class="brand">Brell<span class="brand-sub">Carpentry</span></div>

    <section class="person">
      <h1 class="person-name">Owen Brell</h1>
      <p class="person-role">Qualified Carpenter</p>
      <p class="person-licence">LIC no. 473152c</p>
    </section>

    <section class="contact">
      <p class="contact-phone">042 735 1846</p>
      <p class="contact-email">brellcarpentry@mailvane.com.au</p>
    </section>

    <footer class="tagline-band">
      <span class="tagline tagline--repair">REPAIR IT</span>
      <span class="tagline tagline--build">BUILD IT</span>
      <span class="tagline tagline--fix">FIX IT</span>
    </footer>
  </main>
</body>
</html>
```